Brantley Oakhollow LLC. custom built/handcrafted

I am recent small business owner looking to sell my art(drawings) and woodworking projects from my home. I have a very rough draft of a simple card design created on a simple digital program. I was hoping for a fancier lettering on the initial letters (BO). More of a calligraphy style. Also, the yellow border around the logo I would like to be a gold foil look. For it to be shiny or reflective look and to keep the other letters black with a consistent font on the card and the card white.

Target Market(s)

Local and neighboring cities

Industry/Entity Type

Art (drawing)/Woodworking

Contact Information for Business Card

My email rpoakhollow@mailbright.net, phone number 617-530-4168. In the files provided it has a yellow border around the logo and I was looking to make that a gold foil.

Font styles to use
Serif
Decorative
Script

Requirements
Nice to have
• symbols for having a Friendwall and Snapfolio

```html
<!DOCTYPE html>
<html lang="en">
<head>
<meta charset="utf-8">
<title>Brantley Oakhollow LLC. – Business Card</title>
<link rel="stylesheet" href="https://fonts.googleapis.com/css2?family=Crimson+Text:wght@400;600&display=swap">
<style>
  :root {
    --backdrop: #2a2a2c;
    --card-light-1: #f2f2f1;
    --card-light-2: #cfcfcd;
    --card-dark-1: #2b2b2b;
    --card-dark-2: #111111;
    --ink: #141414;
    --band: #121212;
    --gold: #d9ad2e;
    --paper: #f4f4f2;
  }
  * { margin: 0; padding: 0; box-sizing: border-box; }
  html, body { width: 1200px; height: 1108px; overflow: hidden; }
  body {
    background: var(--backdrop);
    font-family: "Crimson Text", Georgia, serif;
    color: var(--ink);
    position: relative;
  }
  .card {
    position: absolute;
    top: 194px;
    width: 420px;
    height: 720px;
    border-radius: 16px;
    overflow: hidden;
  }
  .card--front { left: 150px; }
  .card--back { left: 630px; }

  .card__grain { position: absolute; inset: 0; }
  .card--front .card__grain {
    background: linear-gradient(100deg, var(--card-light-1), var(--card-light-2) 55%, var(--card-light-1));
  }
  .card--back .card__grain {
    background: linear-gradient(100deg, var(--card-dark-1), var(--card-dark-2) 60%, var(--card-dark-1));
  }

  .card__top-band {
    position: absolute;
    top: 0; left: 52px; right: 30px;
    height: 210px;
    background: var(--band);
  }

  .brand {
    position: absolute;
    left: 0; right: 0;
    display: flex;
    flex-direction: column;
    align-items: center;
  }
  .card--front .brand { top: 78px; }
  .card--back .brand { top: 230px; }
  .brand__disc {
    width: 230px; height: 230px;
    border-radius: 50%;
    display: flex; align-items: center; justify-content: center;
    text-align: center;
    padding: 0 24px;
  }
  .card--front .brand__disc { background: var(--paper); border: 6px solid var(--band); }
  .card--back .brand__disc { border: 6px solid var(--gold); }
  .brand__name {
    font-weight: 600;
    font-size: 26px;
    line-height: 1.2;
    letter-spacing: 1px;
    text-transform: uppercase;
  }
  .card--front .brand__name { color: var(--ink); }
  .card--back .brand__name { color: var(--gold); }

  .contact {
    position: absolute;
    top: 390px; left: 0; right: 0;
    text-align: center;
  }
  .contact__person { font-size: 29px; letter-spacing: 1px; text-transform: uppercase; }
  .contact__role { font-size: 17px; letter-spacing: 1px; text-transform: uppercase; margin-top: 2px; }
  .contact__icons { display: flex; justify-content: center; gap: 10px; margin: 12px 0 8px; }
  .contact__icons svg { width: 24px; height: 24px; }
  .contact__line { font-size: 24px; line-height: 1.25; }

  .social-tab {
    position: absolute;
    bottom: 0; left: 50%;
    transform: translateX(-50%);
    width: 190px; height: 70px;
    background: var(--band);
    border-radius: 10px 10px 0 0;
    display: flex; align-items: center; justify-content: center; gap: 16px;
  }
  .social-tab__item { color: var(--paper); font-size: 16px; }
</style>
</head>
<body>
  <article class="card card--front">
    <div class="card__grain" role="img" aria-label="Light whitewashed wood grain texture"></div>
    <div class="card__top-band"></div>
    <div class="brand">
      <div class="brand__disc"><span class="brand__name">Brantley Oakhollow LLC.</span></div>
    </div>
    <div class="contact">
      <p class="contact__person">Rowan P. Oakhollow</p>
      <p class="contact__role">Owner</p>
      <div class="contact__icons">
        <svg viewBox="0 0 24 24" aria-label="Phone"><circle cx="12" cy="12" r="10.5" fill="none" stroke="#141414" stroke-width="1.4"/><path d="M9 7.5l1.6 2.4-1 1.1a6 6 0 0 0 3.4 3.4l1.1-1 2.4 1.6-.9 1.6c-3.8.2-8-4-7.8-7.8z" fill="#141414"/></svg>
        <svg viewBox="0 0 24 24" aria-label="Email"><circle cx="12" cy="12" r="10.5" fill="none" stroke="#141414" stroke-width="1.4"/><rect x="6.5" y="8.5" width="11" height="7.5" fill="none" stroke="#141414" stroke-width="1.3"/><path d="M6.5 8.5l5.5 4.2 5.5-4.2" fill="none" stroke="#141414" stroke-width="1.3"/></svg>
      </div>
      <p class="contact__line">617-530-4168</p>
      <p class="contact__line">rpoakhollow@mailbright.net</p>
    </div>
    <div class="social-tab">
      <span class="social-tab__item">Snapfolio</span>
      <span class="social-tab__item">Friendwall</span>
    </div>
  </article>

  <article class="card card--back">
    <div class="card__grain" role="img" aria-label="Dark charcoal wood grain texture"></div>
    <div class="brand">
      <div class="brand__disc"><span class="brand__name">Brantley Oakhollow LLC.</span></div>
    </div>
  </article>
</body>
</html>
```